Brevin Finance Flyer Design

I would like a high res flyer designed for mass printing. It is for a mortgage and finance broking company in Sydney. We are called Brevin Finance. The wording i would like displayed is the following
Looking For Something Extra from your broker?
Brevin Finance can make all the difference
What we offer you is an extensive range of mortgage and finance products, including:
• Home Loans
• Investment Loans
• Low Doc Loans
• Vehicle Finance
• Equipment Finance
• Commercial Loans
• Refinance
Contact Us
Phone (02) 7354 2816
email info@brevinfinance.com.au
web www.brevinfinance.com.au
Finance

```html
<!DOCTYPE html>
<html lang="en">
<head>
<meta charset="utf-8">
<title>Brevin Finance Flyer</title>
<link rel="stylesheet" href="https://fonts.googleapis.com/css2?family=Gelasio:wght@400;700&family=Open+Sans:wght@300;400&display=swap">
<style>
  :root {
    --backdrop: #cdcdcd;
    --paper: #ffffff;
    --ink: #2b2626;
    --accent-red: #e3202a;
    --accent-violet: #5350a8;
    --band-dark: #151515;
    --band-mid: #2a2a2a;
    --contact-ink: #333333;
    --logo-ink: #444444;
    --photo-light: #eef5fa;
    --photo-blue: #cfe2f0;
    --photo-deep: #8fa3c4;
  }
  * { margin: 0; padding: 0; box-sizing: border-box; }
  html, body { width: 1200px; height: 1000px; overflow: hidden; }
  body { background: var(--backdrop); position: relative; font-family: "Gelasio", Georgia, serif; }

  .flyer {
    position: absolute; left: 283px; top: 50px;
    width: 633px; height: 898px;
    background: var(--paper);
    overflow: hidden;
  }
  .headline {
    position: absolute; left: 0; top: 45px; width: 100%;
    text-align: center; color: var(--ink);
    font-weight: 700; font-size: 36px; line-height: 42px;
  }
  .hero-photo {
    position: absolute; left: 1px; top: 176px; width: 632px; height: 227px;
    background: linear-gradient(90deg, var(--photo-blue) 0%, var(--photo-light) 30%, #f8fbfd 50%, var(--photo-blue) 75%, var(--photo-deep) 100%);
  }
  .violet-tab {
    position: absolute; left: 41px; top: 379px; width: 328px; height: 24px;
    background: var(--accent-violet);
  }
  .title-band {
    position: absolute; left: 1px; top: 403px; width: 632px; height: 160px;
    background: linear-gradient(180deg, var(--band-mid), var(--band-dark) 50%, var(--band-mid));
    color: var(--paper);
  }
  .title-band .brand {
    position: absolute; left: 49px; top: 16px;
    font-size: 64px; line-height: 80px; font-weight: 400;
  }
  .title-band .tagline {
    position: absolute; left: 49px; top: 94px;
    font-size: 44px; line-height: 50px; font-weight: 400;
    white-space: nowrap;
  }
  .offer-box {
    position: absolute; left: 41px; top: 563px; width: 328px; height: 211px;
    background: var(--accent-red); color: var(--paper);
    padding: 12px 9px 0 9px;
    font-size: 16.5px; line-height: 19px;
  }
  .offer-box .services { list-style: none; margin-top: 19px; }
  .offer-box .services li::before { content: "\2022\00a0"; }
  .contact {
    position: absolute; left: 50px; top: 802px;
    font-family: "Open Sans", Helvetica, Arial, sans-serif;
    font-weight: 300; font-size: 12.5px; line-height: 17px;
    color: var(--contact-ink); font-style: normal;
  }
  .contact .label { font-size: 12px; }
  .company-mark {
    position: absolute; left: 388px; top: 823px;
    display: flex; align-items: center; gap: 8px;
  }
  .company-mark .square { width: 22px; height: 22px; background: var(--logo-ink); }
  .company-mark .name {
    font-family: "Open Sans", Helvetica, Arial, sans-serif;
    font-weight: 400; font-size: 27px; line-height: 30px; color: var(--logo-ink);
  }
  .company-mark .sub {
    position: absolute; left: 30px; top: 31px; white-space: nowrap;
    font-family: "Open Sans", Helvetica, Arial, sans-serif;
    font-size: 9.5px; color: var(--logo-ink);
  }
</style>
</head>
<body>
  <main class="flyer">
    <h1 class="headline">Looking For Something Extra<br>from your broker?</h1>

    <div class="hero-photo" role="img" aria-label="Photo of business people walking through a bright glass office corridor"></div>
    <div class="violet-tab"></div>

    <section class="title-band">
      <p class="brand">Brevin Finance</p>
      <p class="tagline">can make all the difference</p>
    </section>

    <section class="offer-box">
      <p>What we offer you is an extensive range of mortgage and finance products, including:</p>
      <ul class="services">
        <li>Home Loans</li>
        <li>Investment Loans</li>
        <li>Low Doc Loans</li>
        <li>Vehicle Finance</li>
        <li>Equipment Finance</li>
        <li>Commercial Loans</li>
        <li>Refinance</li>
      </ul>
    </section>

    <address class="contact">
      <span class="label">Contact Us</span><br>
      Phone (02) 7354 2816<br>
      email info@brevinfinance.com.au<br>
      web www.brevinfinance.com.au
    </address>

    <div class="company-mark">
      <span class="square"></span>
      <span class="name">Brevin Finance</span>
      <span class="sub">mortgage and finance broking services</span>
    </div>
  </main>
</body>
</html>
```